Popup Nightclub Grand Opening Flyer

We need to design a flyer for the grand opening of an upscale, exclusive nightclub called "Lanternfall". The design needs to be chic and exclusive. The background should be black and the text should primarily be white. We like minimalist designs.

Here is the text for the flyer
-
Velvetrope Atlanta Presents

Lanternfall (LOGO)

A Popup Nightclub Experience
For one night Only

Friday, October 18, 2013
Party begins at 9PM

INVITE ONLY

See invitation for location details
(Velvetrope Atlanta logo)

-
Examples we like

http://cdn2-b.brivelpost.com/sites/default/files/styles/image_content_width/hash/3d/fa/1472093815_4471_flyer.jpg?itok=R8kqWm2z

http://api.plovra.com/files/7Kqq-Tr82XXB3pQzJvmtR5HL2W719E4nbRtC6KLd4HsfM8Y2qTDK-VmjwDoNqLX4QBzTHD9nakRbVx3m-Pfq8htc3MDTWr5p4/2zelSaturdays.jpg

http://quenmar.com/wp-content/uploads/yootheme/widgetkit/gallery/2zel/2zel-gen_vroom4-01.jpg

Hi All, one thing that we are seeing that we don't like is on over emphasis on the phrase "a popup nightclub experience" please don't make this the largest thing on the flyer

Target Market(s)

Target market is 25-35 year olds who are affluent (rich) and like luxury brands

Requirements
Must have
• Dark Background
Nice to have
• Velvetrope Logo on the bottom
Modern text that isn't curvy
Should not have
• Curved text

```html
<!DOCTYPE html>
<html lang="en">
<head>
<meta charset="utf-8">
<title>Lanternfall Nightclub – Invite Only</title>
<link href="https://fonts.googleapis.com/css2?family=Cinzel:wght@400;700&family=Josefin+Sans:wght@300;400&family=Oswald:wght@400;500&family=Pinyon+Script&display=swap" rel="stylesheet">
<style>
  :root {
    --plum-core: #46324a;
    --plum-mid: #2f1f33;
    --plum-edge: #140a16;
    --ink: #ffffff;
    --ink-soft: #e9e4ea;
    --mark-tone: #e6e3e8;
    --rule: rgba(255,255,255,0.28);
  }
  html, body {
    margin: 0;
    padding: 0;
    width: 900px;
    height: 1200px;
    overflow: hidden;
    background: var(--plum-edge);
  }
  .flyer {
    position: relative;
    width: 900px;
    height: 1200px;
    overflow: hidden;
    background: radial-gradient(ellipse 62% 52% at 50% 40%, var(--plum-core) 0%, var(--plum-mid) 55%, var(--plum-edge) 100%);
    color: var(--ink);
  }
  .presenter {
    position: absolute;
    top: 58px;
    left: 0;
    width: 100%;
    text-align: center;
    font-family: "Cinzel", serif;
    font-size: 14px;
    letter-spacing: 0.06em;
    color: var(--ink-soft);
  }
  .presenter .host { font-weight: 700; }
  .presenter .divider {
    width: 545px;
    height: 1px;
    margin: 8px auto 6px;
    background: linear-gradient(90deg, transparent, var(--rule) 20%, var(--rule) 80%, transparent);
  }
  .date {
    position: absolute;
    top: 160px;
    right: 94px;
    text-align: right;
  }
  .date .weekday {
    font-family: "Cinzel", serif;
    font-size: 30px;
    letter-spacing: 0.3em;
    margin-right: -0.3em;
    line-height: 1;
  }
  .date .numbers {
    font-family: "Oswald", sans-serif;
    font-weight: 400;
    font-size: 56px;
    line-height: 1;
    margin-top: 4px;
    letter-spacing: -0.04em;
  }
  .club-mark {
    position: absolute;
    top: 290px;
    left: 260px;
    width: 380px;
    height: 380px;
  }
  .venue {
    position: absolute;
    top: 712px;
    left: 0;
    width: 100%;
    text-align: center;
    font-family: "Josefin Sans", sans-serif;
    font-weight: 300;
    color: var(--ink);
  }
  .venue .name {
    font-size: 34px;
    letter-spacing: 0.14em;
    margin-right: -0.14em;
    line-height: 1;
  }
  .venue .kind {
    margin-top: 10px;
    font-size: 16px;
    font-weight: 400;
    letter-spacing: 0.14em;
    margin-right: -0.14em;
  }
  .access {
    position: absolute;
    top: 790px;
    left: 0;
    width: 100%;
    height: 190px;
  }
  .access .invite {
    position: absolute;
    left: 205px;
    top: 0;
    font-family: "Pinyon Script", cursive;
    font-size: 160px;
    line-height: 1;
  }
  .access .only {
    position: absolute;
    left: 505px;
    top: 158px;
    font-family: "Cinzel", serif;
    font-size: 32px;
    letter-spacing: 0.2em;
    line-height: 1;
  }
  .start-time {
    position: absolute;
    top: 1043px;
    left: 50%;
    transform: translateX(-50%);
    padding: 6px 2px;
    border-top: 1px solid var(--rule);
    border-bottom: 1px solid var(--rule);
    font-family: "Oswald", sans-serif;
    font-weight: 500;
    font-size: 26px;
    line-height: 1.1;
    white-space: nowrap;
  }
  .location-note {
    position: absolute;
    top: 1096px;
    left: 0;
    width: 100%;
    text-align: center;
    font-family: "Josefin Sans", sans-serif;
    font-weight: 300;
    font-size: 12px;
    letter-spacing: 0.16em;
    color: var(--ink-soft);
  }
  .host-mark {
    position: absolute;
    top: 1130px;
    left: 0;
    width: 100%;
    display: flex;
    justify-content: center;
    align-items: center;
    gap: 12px;
    font-family: "Josefin Sans", sans-serif;
    font-weight: 400;
    font-size: 18px;
    letter-spacing: 0.16em;
    color: var(--ink-soft);
  }
  .host-mark .dot {
    width: 20px;
    height: 20px;
    border-radius: 50%;
    background: var(--ink-soft);
  }
</style>
</head>
<body>
  <main class="flyer">
    <header class="presenter">
      <div><span class="host">VELVETROPE ATLANTA</span> PRESENTS</div>
      <div class="divider"></div>
      <div>A POPUP NIGHTCLUB EXPERIENCE…FOR ONE NIGHT ONLY</div>
    </header>

    <section class="date">
      <div class="weekday">FRIDAY</div>
      <div class="numbers">10|18|2013</div>
    </section>

    <svg class="club-mark" viewBox="0 0 380 380" role="img" aria-label="Lanternfall nightclub logo">
      <circle cx="190" cy="190" r="190" fill="var(--mark-tone)"/>
    </svg>

    <section class="venue">
      <div class="name">LANTERNFALL</div>
      <div class="kind">NIGHTCLUB</div>
    </section>

    <section class="access">
      <span class="invite">Invite</span>
      <span class="only">ONLY</span>
    </section>

    <div class="start-time">PARTY BEGINS AT 9PM</div>

    <p class="location-note">SEE INVITATION FOR LOCATION DETAILS</p>

    <footer class="host-mark">
      <span class="dot"></span>
      <span>VELVETROPE ATLANTA</span>
    </footer>
  </main>
</body>
</html>
```